Electrical Contracting Business Website

Require website done for my contracting business.
Partly done one but really dont have time.

You can view the current one at http://brelton.net.au

You can use any info/styles/photos from the current website

I like the orange color of the logo so id like things to be with that
Unfortunatly being a new business (Sept 2015) I havent got alot of photos . but if you require any for any of the specifics listed in the doc file ill have a look to see what I have.

I am targeting mainly commercial / industrial clients. Which also includes government and mining.

Target Market(s)

People requiring electricians

Industry/Entity Type

Electrician

Coding

Number of Pages Required

Colors
f37122

Requirements
Must have
• logo with EC Number
• Keep it simple and not to complicated
• Comply with the current html / style sheet standards.
• Desktop/Mobile Version compatability
Nice to have
• additional photos.
• The domestic lifts we install are by vostrel I dont have any photos of them unfortunately.
Should not have
• change colour of logo

```html
<!DOCTYPE html>
<html lang="en">
<head>
<meta charset="utf-8">
<title>Brelton Engineering — Specialized Electrical Services</title>
<link href="https://fonts.googleapis.com/css2?family=Roboto:wght@400;500;700&family=Arimo:ital,wght@0,400;0,700;1,400&display=swap" rel="stylesheet">
<style>
:root{
  --orange:#ef5a28;
  --orange-dark:#d9481b;
  --ink:#333;
  --muted:#8a8a8a;
  --soft:#efefef;
  --line:#d6d6d6;
  --white:#fff;
}
*{box-sizing:border-box;margin:0;padding:0}
html,body{width:1200px;height:2616px;overflow:hidden;background:var(--white)}
body{position:relative;font-family:"Arimo",Arial,sans-serif;color:var(--ink)}
.abs{position:absolute}
h1,h2,h3,.nav a,.btn{font-family:"Roboto",Arial,sans-serif;font-weight:400}

/* header */
.site-header{position:absolute;left:0;top:0;width:1200px;height:136px;background:var(--white);border-top:3px solid var(--orange)}
.brand{position:absolute;left:78px;top:18px;display:flex;align-items:center;gap:12px}
.brand-mark{width:64px;height:64px;border-radius:50%;background:var(--orange)}
.brand-name{font-family:"Roboto",sans-serif;font-weight:700;font-size:44px;color:var(--orange);line-height:1;letter-spacing:-1px}
.brand-meta{position:absolute;left:146px;top:96px;font-size:9px;line-height:11px;color:var(--orange);font-weight:700}
.nav{position:absolute;left:372px;top:0;height:133px;display:flex}
.nav a{display:flex;align-items:center;height:100%;padding:0 21px;font-size:16px;color:#333;text-decoration:none;text-transform:uppercase}
.nav a.active{background:var(--orange);color:var(--white);padding:0 24px}

/* hero */
.hero{position:absolute;left:0;top:136px;width:1200px;height:539px;background:linear-gradient(100deg,#4a4e55 0%,#8c9096 28%,#c9ccd0 42%,#3e4654 60%,#2a3a66 80%,#394a74 100%)}
.hero-title{position:absolute;left:0;width:1200px;top:222px;text-align:center;font-size:53px;font-weight:500;color:var(--orange);text-transform:uppercase}
.hero-sub{position:absolute;left:0;width:1200px;top:296px;text-align:center;font-size:31px;font-weight:700;color:var(--orange);font-family:"Roboto",sans-serif}
.hero-sub b{color:var(--white)}
.arrow{position:absolute;top:228px;width:52px;height:52px;border:2px solid var(--white);border-radius:50%;background:rgba(0,0,0,.3)}
.arrow.prev{left:12px}.arrow.next{right:12px}
.arrow svg{width:100%;height:100%}

/* services */
.service{position:absolute;top:610px;width:332px;height:385px;background:var(--white)}
.service .photo{margin:10px 10px 0;height:208px}
.service h3{margin:30px 0 0 12px;font-size:20px;color:var(--orange)}
.service p{margin:12px 12px 0;font-size:14px;line-height:25px;color:var(--muted)}
.readmore{display:block;margin:8px 0 0 12px;font-size:14px;font-style:italic;color:#333}
.divider{position:absolute;left:77px;top:1044px;width:1046px;height:4px;background:#f1f1f1}

/* welcome */
.welcome h2{position:absolute;left:0;top:1100px;width:1200px;text-align:center;font-size:41px;color:var(--orange)}
.welcome p{position:absolute;left:125px;top:1160px;width:950px;text-align:center;font-size:14px;line-height:27px;color:var(--muted)}
.btn{position:absolute;display:flex;align-items:center;justify-content:center;background:var(--orange);color:var(--white);font-size:20px;text-transform:uppercase}
.btn.know{left:506px;top:1308px;width:186px;height:60px}

/* about */
.about{position:absolute;left:0;top:1434px;width:1200px;height:462px;background:var(--soft)}
.about h2{position:absolute;left:0;top:55px;width:1200px;text-align:center;font-size:41px;color:var(--orange)}
.about .lead{position:absolute;left:170px;top:112px;width:860px;text-align:center;font-size:14px;line-height:26px;color:#555}
.value{position:absolute;top:182px;width:230px;text-align:center}
.value .icon{width:98px;height:98px;margin:0 auto;border-radius:50%;background:var(--orange)}
.value h3{margin-top:30px;font-size:20px;color:var(--orange);text-transform:uppercase}
.value p{margin-top:8px;font-size:14px;line-height:23px;color:#444}

/* project + contact */
.section-title{position:absolute;top:1955px;font-size:38px;color:var(--orange);font-family:"Roboto",sans-serif;text-transform:uppercase}
.project-card{position:absolute;left:64px;top:1950px;width:508px;height:405px;box-shadow:10px 0 12px -8px rgba(0,0,0,.2)}
.project-photo{position:absolute;left:77px;top:2020px;width:207px;height:156px;background:linear-gradient(120deg,#b9bcc2,#5d6470 55%,#2b3d75)}
.project-name{position:absolute;left:301px;top:2020px;font-size:20px;color:var(--orange);font-family:"Roboto",sans-serif;text-transform:uppercase}
.project-desc{position:absolute;left:301px;top:2054px;width:270px;font-size:15px;line-height:22px;color:#444}
.project-row{position:absolute;left:301px;font-size:14px;color:#666}
.project-row span{display:inline-block;width:82px;color:var(--orange)}
.partner-badge{position:absolute;left:78px;top:2224px;width:176px;height:92px;background:#dfe6f0;border-radius:4px}
.field{position:absolute;left:610px;width:512px;height:47px;border:1px solid var(--line);font-size:14px;color:#888;padding:14px 16px}
.field svg{position:absolute;right:12px;top:14px;width:18px;height:18px}
.field.message{height:102px}
.btn.submit{left:790px;top:2295px;width:167px;height:56px}

/* footer */
.site-footer{position:absolute;left:0;top:2414px;width:1200px;height:202px;background:var(--orange);color:var(--white)}
.foot-nav{position:absolute;left:77px;top:18px;display:flex;gap:0}
.foot-nav a{font-size:16px;color:var(--white);text-decoration:none;padding:12px 16px;border:2px solid transparent}
.foot-nav a.active{border-color:var(--white);padding:12px 22px}
.social{position:absolute;top:16px;width:52px;height:52px;border:2px solid var(--white);border-radius:50%}
.social.solid{background:var(--white)}
.foot-rule{position:absolute;left:77px;top:84px;width:1046px;height:1px;background:rgba(255,255,255,.5)}
.foot-contact{position:absolute;top:116px;display:flex;align-items:center;gap:18px;font-size:16px}
.foot-contact .dot{width:56px;height:56px;border-radius:50%;background:var(--white);display:flex;align-items:center;justify-content:center}
.foot-contact svg{width:26px;height:26px}
.copyright{position:absolute;left:876px;top:130px;width:260px;font-size:14px;line-height:22px}
.copyright b{color:#3a1a10;font-weight:700}
</style>
</head>
<body>

<header class="site-header">
  <div class="brand"><div class="brand-mark"></div><div class="brand-name">BRELTON</div></div>
  <div class="brand-meta">ACN: 612 408 559<br>ABN: 41 612 408 559 &nbsp; EC UC: 40317</div>
  <nav class="nav">
    <a class="active">Home</a><a>Residential</a><a>Commercial</a><a>Industrial</a><a>About Us</a><a>Contact Us</a>
  </nav>
</header>

<section class="hero" role="img" aria-label="Close view of a switchboard with breakers and blue wiring">
  <div class="arrow prev"><svg viewBox="0 0 52 52"><path d="M30 16 L20 26 L30 36" fill="none" stroke="#fff" stroke-width="2.5"/></svg></div>
  <div class="arrow next"><svg viewBox="0 0 52 52"><path d="M22 16 L32 26 L22 36" fill="none" stroke="#fff" stroke-width="2.5"/></svg></div>
  <h1 class="hero-title">Specialized Electrical Services</h1>
  <div class="hero-sub">Call <b>0491 306 722</b> For a Quote</div>
</section>

<article class="service" style="left:77px">
  <div class="photo" role="img" aria-label="Electrician fitting a switch box between timber studs" style="background:linear-gradient(135deg,#c7986a,#8a6a4e 60%,#5a4a40)"></div>
  <h3>RESIDENTIAL</h3>
  <p>Lorem Ipsum is simply dummy text of the printing and typesetting industry. Lorem Ipsum has been the industry's standard</p>
  <span class="readmore">READ MORE.. »</span>
</article>
<article class="service" style="left:432px">
  <div class="photo" role="img" aria-label="Commercial control panel with rows of modules" style="background:linear-gradient(135deg,#d5d6d8,#8f9294 55%,#5b6064)"></div>
  <h3>COMMERCIAL</h3>
  <p>Lorem Ipsum is simply dummy text of the printing and typesetting industry. Lorem Ipsum has been the industry's standard</p>
  <span class="readmore">READ MORE.. »</span>
</article>
<article class="service" style="left:790px">
  <div class="photo" role="img" aria-label="Technician testing an industrial board with a multimeter" style="background:linear-gradient(135deg,#3a3f4a,#5f6b7a 45%,#2d6fb8)"></div>
  <h3>INDUSTRIAL</h3>
  <p>Lorem Ipsum is simply dummy text of the printing and typesetting industry. Lorem Ipsum has been the industry's standard</p>
  <span class="readmore">READ MORE.. »</span>
</article>
<div class="divider"></div>

<section class="welcome">
  <h2>WELCOME TO BRELTON ENGINEERING</h2>
  <p>Lorem Ipsum is simply dummy text of the printing and typesetting industry. Lorem Ipsum has been the industry's standard dummy text ever since the 1500s, when an unknown printer took a galley of type and scrambled it to make a type specimen book. It has survived not only five centuries, but also the leap into electronic typesetting, remaining essentially unchanged. It was popularised in the 1960s with the release of Letraset sheets containing Lorem Ipsum passages. It was popularised in the 1960s with the release of Letraset sheets containing Lorem Ipsum passages. It was popularised in the 1960s</p>
  <div class="btn know">Know More</div>
</section>

<section class="about">
  <h2>ABOUT US</h2>
  <p class="lead">Lorem Ipsum is simply dummy text of the printing and typesetting industry. Lorem Ipsum has been the industry's standard dummy text ever since the 1500s, when an unknown printer took.</p>
  <div class="value" style="left:91px">
    <svg class="icon" viewBox="0 0 98 98"><circle cx="49" cy="49" r="49" fill="#ef5a28"/><circle cx="49" cy="49" r="24" fill="none" stroke="#fff" stroke-width="4"/><circle cx="49" cy="49" r="13" fill="none" stroke="#fff" stroke-width="4"/><circle cx="49" cy="49" r="4" fill="#fff"/><path d="M49 49 L70 28" stroke="#fff" stroke-width="3"/></svg>
    <h3>Our Values</h3><p>Lorem Ipsum is simply dummy text of the printing and type setting industry.</p>
  </div>
  <div class="value" style="left:356px">
    <svg class="icon" viewBox="0 0 98 98"><circle cx="49" cy="49" r="49" fill="#ef5a28"/><path d="M49 24 L70 31 V48 C70 62 60 70 49 75 C38 70 28 62 28 48 V31 Z" fill="none" stroke="#fff" stroke-width="3.5"/><path d="M49 30 V70 M33 48 H65" stroke="#fff" stroke-width="3"/></svg>
    <h3>Safety</h3><p>Lorem Ipsum is simply dummy text of the printing and type setting industry.</p>
  </div>
  <div class="value" style="left:621px">
    <svg class="icon" viewBox="0 0 98 98"><circle cx="49" cy="49" r="49" fill="#ef5a28"/><rect x="28" y="46" width="10" height="24" fill="#fff"/><path d="M42 46 L52 26 C57 26 58 30 57 36 L55 44 H68 C72 44 73 48 71 51 L66 68 C65 70 63 70 61 70 H42 Z" fill="#fff"/></svg>
    <h3>Quality</h3><p>Lorem Ipsum is simply dummy text of the printing and type setting industry.</p>
  </div>
  <div class="value" style="left:886px">
    <svg class="icon" viewBox="0 0 98 98"><circle cx="49" cy="49" r="49" fill="#ef5a28"/><path d="M22 44 L36 32 L50 38 L62 32 L76 44 L64 60 L52 68 L36 58 Z" fill="none" stroke="#fff" stroke-width="3.5" stroke-linejoin="round"/><path d="M44 46 L56 56" stroke="#fff" stroke-width="3"/></svg>
    <h3>Reliability</h3><p>Lorem Ipsum is simply dummy text of the printing and type setting industry.</p>
  </div>
</section>

<section class="project">
  <div class="project-card"></div>
  <h2 class="section-title" style="left:80px">Recent Project</h2>
  <div class="project-photo" role="img" aria-label="Hoist control board with breakers and wiring"></div>
  <div class="project-name">Trelo Liftdeck 5000</div>
  <div class="project-desc">Cmmissioning and maintenance of a5 tonne Materials hoist</div>
  <div class="project-row" style="top:2108px"><span>Client</span>: Lindmark Hoists</div>
  <div class="project-row" style="top:2145px"><span>Location :</span> Carrow Build Group</div>
  <div class="partner-badge" aria-label="Industry association membership"></div>
</section>

<section class="contact">
  <h2 class="section-title" style="left:610px">Contact Us</h2>
  <div class="field" style="top:2017px">Name<svg viewBox="0 0 18 18"><circle cx="9" cy="5" r="4" fill="#999"/><path d="M2 17 C2 11 16 11 16 17 Z" fill="#999"/></svg></div>
  <div class="field" style="top:2071px">Email<svg viewBox="0 0 18 18"><path d="M4 2 L7 2 L8 6 L6 8 C7 10 8 11 10 12 L12 10 L16 11 L16 14 C16 15 15 16 14 16 C7 16 2 11 2 4 C2 3 3 2 4 2 Z" fill="#999"/></svg></div>
  <div class="field" style="top:2125px">Phone<svg viewBox="0 0 18 18"><rect x="1" y="4" width="16" height="11" fill="#999"/><path d="M1 4 L9 10 L17 4" fill="none" stroke="#fff" stroke-width="1.5"/></svg></div>
  <div class="field message" style="top:2180px">Message<svg viewBox="0 0 18 18"><path d="M2 3 H14 V11 H7 L4 14 V11 H2 Z" fill="#999"/></svg></div>
  <div class="btn submit">Submit</div>
</section>

<footer class="site-footer">
  <nav class="foot-nav"><a class="active">Home</a><a>Residential</a><a>Commercial</a><a>Industrial</a><a>About Us</a><a>Contact Us</a></nav>
  <div class="social solid" style="left:946px" aria-label="Social profile"></div>
  <div class="social" style="left:1008px" aria-label="Social profile"></div>
  <div class="social" style="left:1070px" aria-label="Social profile"></div>
  <div class="foot-rule"></div>
  <div class="foot-contact" style="left:77px"><span class="dot"><svg viewBox="0 0 18 18"><path d="M4 2 L7 2 L8 6 L6 8 C7 10 8 11 10 12 L12 10 L16 11 L16 14 C16 15 15 16 14 16 C7 16 2 11 2 4 C2 3 3 2 4 2 Z" fill="#ef5a28"/></svg></span>0491 306 722</div>
  <div class="foot-contact" style="left:343px"><span class="dot"><svg viewBox="0 0 18 18"><rect x="4" y="2" width="10" height="5" fill="none" stroke="#ef5a28" stroke-width="1.5"/><rect x="2" y="7" width="14" height="9" rx="1" fill="#ef5a28"/><rect x="5" y="10" width="8" height="3" fill="#fff"/></svg></span>08 7140 29 36</div>
  <div class="foot-contact" style="left:607px"><span class="dot"><svg viewBox="0 0 18 18"><rect x="1" y="4" width="16" height="11" fill="#ef5a28"/><path d="M1 4 L9 10 L17 4" fill="none" stroke="#fff" stroke-width="1.5"/></svg></span>info@brelton.net.au</div>
  <div class="copyright">© 2016 <b>Brelton Engineering Pty Ltd</b> - All rights reserved. EC 40317</div>
</footer>

</body>
</html>
```